Business Card & Word Docs from existing Logo

We need a business card with typical information plus layout to include electrical contractors license number, VORLE license and KMT license. We would like a word document layout for a proposal document, opening page with logo and design basic information; proposal to and proposal from and project name and number. Small basic single page letter for general documents. Email signature with logo.

We are an electrical, refrigeration and automation contractor. We work with reducing energy consumption for our customers and complex process solutions in electrical, refrigeration and automation.
Updates

Reason: Final changes/ revisions to designs.

Target Market(s)

Industrial and commercial businesses that require more than your average contractor.

Industry/Entity Type

Electrical

Requirements
Must have
• Propsal document must have a full opening page.

```html
<!DOCTYPE html>
<html lang="en">
<head>
<meta charset="utf-8">
<title>Frostline Contracting – Proposal Pages</title>
<link rel="stylesheet" href="https://fonts.googleapis.com/css2?family=Open+Sans:wght@400;600;700&family=Roboto+Condensed:wght@400;700&display=swap">
<style>
  :root {
    --backdrop: #1d1b1a;
    --brand-blue: #2a6ea0;
    --brand-teal: #157a73;
    --brand-green: #008c3a;
    --logo-green: #2b9a45;
    --paper: #ffffff;
    --ink: #222222;
    --footer-grey: #666666;
    --rule: #b9c4cc;
    --panel-blue: #e6eef6;
    --panel-green: #e6f2ea;
  }
  * { box-sizing: border-box; margin: 0; padding: 0; }
  html, body { width: 1200px; height: 900px; overflow: hidden; }
  body {
    background: var(--backdrop);
    position: relative;
    font-family: "Open Sans", Arial, sans-serif;
  }
  .page {
    position: absolute;
    top: 75px;
    width: 530px;
    height: 750px;
    overflow: hidden;
  }
  .cover {
    left: 42px;
    background: linear-gradient(90deg, var(--brand-blue) 0%, var(--brand-blue) 30%, var(--brand-teal) 58%, var(--brand-green) 85%, var(--brand-green) 100%);
  }
  .cover .decoration { position: absolute; left: 0; top: 0; }
  .cover-header {
    position: absolute;
    left: 38px; top: 30px;
    width: 462px; height: 88px;
    border-radius: 0 10px 0 0;
    background: linear-gradient(100deg, rgba(255,255,255,0) 0%, rgba(255,255,255,0.55) 30%, #ffffff 52%, #ffffff 100%);
  }
  .brand {
    position: absolute;
    display: flex; align-items: center; gap: 6px;
    font-family: "Roboto Condensed", Arial, sans-serif;
    font-weight: 700;
    color: var(--logo-green);
    letter-spacing: 0.2px;
    white-space: nowrap;
  }
  .brand-dot { border-radius: 50%; background: var(--logo-green); flex: none; }
  .cover-header .brand { right: 12px; top: 14px; font-size: 17px; }
  .cover-header .brand-dot { width: 22px; height: 22px; }
  .contact {
    position: absolute;
    right: 12px; top: 55px;
    text-align: right;
    font-family: "Roboto Condensed", Arial, sans-serif;
    font-size: 7.2px;
    line-height: 8.6px;
    color: var(--ink);
  }
  .contact b { font-weight: 700; }
  .field { position: absolute; }
  .field-label {
    display: block;
    font-size: 7.5px;
    font-weight: 700;
    color: #ffffff;
    margin-bottom: 1px;
  }
  .field-box {
    display: block;
    height: 22px;
    background: #ffffff;
    border-radius: 0 9px 0 0;
  }
  .field-to { left: 30px; top: 145px; width: 226px; }
  .field-from { left: 274px; top: 145px; width: 226px; }
  .field-project { left: 30px; top: 191px; width: 332px; }
  .field-number { left: 380px; top: 191px; width: 120px; }
  .page-footer {
    position: absolute;
    right: 30px;
    font-family: "Roboto Condensed", Arial, sans-serif;
    font-size: 7px;
    white-space: nowrap;
  }
  .page-footer b { font-weight: 700; }
  .cover .page-footer { bottom: 14px; color: #ffffff; }

  .letter { left: 628px; background: var(--paper); }
  .letter-panel {
    position: absolute;
    left: 30px; top: 30px;
    width: 470px; height: 692px;
    border-radius: 0 0 0 9px;
    background: linear-gradient(160deg, var(--panel-blue) 0%, #f4f8fb 40%, #f7faf8 60%, var(--panel-green) 100%);
    overflow: hidden;
  }
  .letter-panel .decoration { position: absolute; left: 0; top: 0; }
  .letter .brand { right: 40px; top: 44px; font-size: 10px; }
  .letter .brand-dot { width: 14px; height: 14px; }
  .writing-lines {
    position: absolute;
    left: 12px; right: 12px; top: 61px;
    height: 610px;
    background-image: repeating-linear-gradient(180deg, transparent 0, transparent 16.6px, var(--rule) 16.6px, var(--rule) 17.6px);
    -webkit-mask-image: repeating-linear-gradient(90deg, #000 0, #000 1.5px, transparent 1.5px, transparent 3px);
    mask-image: repeating-linear-gradient(90deg, #000 0, #000 1.5px, transparent 1.5px, transparent 3px);
  }
  .letter .page-footer { bottom: 14px; color: var(--footer-grey); }
</style>
</head>
<body>

<section class="page cover" aria-label="Proposal cover page">
  <svg class="decoration" width="530" height="750" viewBox="0 0 530 750" role="img" aria-label="Large faint brand emblem decoration">
    <defs>
      <radialGradient id="emblemGlow" cx="0.3" cy="0.7" r="0.8">
        <stop offset="0" stop-color="#ffffff" stop-opacity="0.75"/>
        <stop offset="0.5" stop-color="#ffffff" stop-opacity="0.35"/>
        <stop offset="1" stop-color="#ffffff" stop-opacity="0.15"/>
      </radialGradient>
    </defs>
    <circle cx="440" cy="650" r="405" fill="url(#emblemGlow)"/>
  </svg>

  <header class="cover-header">
    <div class="brand"><span class="brand-dot"></span>FROSTLINE CONTRACTING</div>
    <p class="contact">
      PO Box 5678, Townsville, Queensland, 4810<br>
      <b>T</b> 07 5550 1020 | <b>F</b> 07 5550 1021 | <b>M</b> 0400 555 789<br>
      sam@frostline.com.au | www.frostline.com.au
    </p>
  </header>

  <div class="field field-to"><span class="field-label">Proposal to</span><span class="field-box"></span></div>
  <div class="field field-from"><span class="field-label">Proposal from</span><span class="field-box"></span></div>
  <div class="field field-project"><span class="field-label">Project name</span><span class="field-box"></span></div>
  <div class="field field-number"><span class="field-label">Number</span><span class="field-box"></span></div>

  <footer class="page-footer"><b>FROSTLINE CONTRACTING</b> Page 1 of X</footer>
</section>

<section class="page letter" aria-label="Proposal continuation page">
  <div class="letter-panel">
    <svg class="decoration" width="470" height="692" viewBox="0 0 470 692" role="img" aria-label="Faint brand emblem watermark">
      <defs>
        <radialGradient id="watermarkGlow" cx="0.4" cy="0.6" r="0.7">
          <stop offset="0" stop-color="#ffffff" stop-opacity="0.8"/>
          <stop offset="1" stop-color="#ffffff" stop-opacity="0.3"/>
        </radialGradient>
      </defs>
      <circle cx="400" cy="640" r="400" fill="url(#watermarkGlow)"/>
    </svg>
    <div class="writing-lines"></div>
  </div>
  <div class="brand"><span class="brand-dot"></span>FROSTLINE CONTRACTING</div>
  <footer class="page-footer"><b>FROSTLINE CONTRACTING</b> Page 2 of X</footer>
</section>

</body>
</html>
```